Medical device box for kits used for self testing purposes. Attractive simplistic design

Looking for a design that will go on a box that offer multiple range of medical testing ranging from hormones panel to diabetes and thyroid hormones. looking for something attractive and simple to go on a box 6 x 4.5 x 1 inches. attached are some examples from competitors. and our logo that be incorporated with the design.
Picture of the boxes have been attached, pick the color you think goes best with your design.

Target Market(s)

Patients and regular consumers

Industry/Entity Type

Medical

Requirements
Nice to have
• Simple design that is eye catching

```html
<!DOCTYPE html>
<html lang="en">
<head>
<meta charset="UTF-8">
<title>Medical Test Box Lid</title>
<link rel="stylesheet" href="https://fonts.googleapis.com/css2?family=Montserrat:wght@700&display=swap">
<style>
  :root {
    --page-bg: #ffffff;
    --navy: #0f163a;
    --teal: #1c8fa3;
    --red: #e0303c;
    --orange: #f5a31f;
    --purple: #7e2168;
    --blue: #1e6fb0;
    --green: #2bb596;
  }
  html, body {
    margin: 0;
    padding: 0;
    width: 800px;
    height: 1200px;
    overflow: hidden;
    background: var(--page-bg);
  }
  .canvas {
    position: relative;
    width: 800px;
    height: 1200px;
  }
  .lid {
    position: absolute;
    left: 40px;
    top: 270px;
    width: 720px;
    height: 660px;
    background: var(--navy);
    overflow: hidden;
    font-family: "Montserrat", sans-serif;
    font-weight: 700;
    color: var(--teal);
  }
  .lid__artwork {
    position: absolute;
    left: 0;
    top: 0;
    width: 350px;
    height: 410px;
    background: linear-gradient(135deg,
      var(--red) 0%,
      var(--orange) 25%,
      var(--blue) 45%,
      var(--purple) 62%,
      var(--green) 80%,
      var(--navy) 100%);
    clip-path: polygon(0 0, 100% 0, 100% 35%, 55% 100%, 0 100%);
    opacity: 0.9;
  }
  .lid__title {
    position: absolute;
    right: 77px;
    top: 95px;
    margin: 0;
    text-align: right;
    font-size: 49px;
    line-height: 48px;
    letter-spacing: 0.5px;
    font-weight: 700;
  }
  .lid__tab {
    position: absolute;
    left: 660px;
    top: 99px;
    width: 60px;
    height: 84px;
    background: var(--teal);
  }
  .brand {
    position: absolute;
    display: flex;
    align-items: center;
    gap: 10px;
    color: var(--teal);
    font-weight: 700;
    line-height: 1;
  }
  .brand__dot {
    flex: none;
    border-radius: 50%;
    background: var(--teal);
  }
  .brand--main {
    right: 34px;
    top: 444px;
    height: 50px;
    font-size: 40px;
  }
  .brand--main .brand__dot { width: 30px; height: 30px; }
  .brand--small {
    left: 49px;
    top: 581px;
    height: 38px;
    font-size: 27px;
    gap: 7px;
  }
  .brand--small .brand__dot { width: 20px; height: 20px; }
  .lid__footer-title {
    position: absolute;
    right: 64px;
    top: 579px;
    margin: 0;
    font-size: 32px;
    line-height: 34px;
    letter-spacing: 0.5px;
  }
</style>
</head>
<body>
<div class="canvas">
  <section class="lid">
    <div class="lid__artwork" role="img" aria-label="Colourful diagonal capsules and rings in red, orange, blue, purple and green"></div>

    <h1 class="lid__title">MEDICAL<br>TEST</h1>
    <div class="lid__tab"></div>

    <div class="brand brand--main">
      <span class="brand__dot"></span>
      <span class="brand__name">Qelvo</span>
    </div>

    <div class="brand brand--small">
      <span class="brand__dot"></span>
      <span class="brand__name">Qelvo</span>
    </div>

    <p class="lid__footer-title">MEDICAL TEST</p>
  </section>
</div>
</body>
</html>
```